I need a CD cover (simple single CD -- NOT jewel case) for my new CD. This is a very small independent project -- probably 100 - 200 copies to be made in total. The name of the CD is "Folded Lanterns". My name (artist) is ned valko (I prefer lower case for my name). I just want an interesting design on the front cover that has both the CD name and my name (no photo) -- just something that looks cool -- I'm open to any and all ideas. The back should contain the enclosed photo -- I am open to the photo being any size -- even very small if that looks best. The front cover design will also need to be ON the CD itself (adapted as needed). I am not concerned with the design of the front having any relationship to the music -- I just want something that is attractive and looks cool.
Look and feel
Each slider illustrates characteristics of the customer's brand and the style your logo design should communicate.

```html
<!DOCTYPE html>
<html lang="en">
<head>
<meta charset="utf-8">
<title>Folded Lanterns — ned valko</title>
<link href="https://fonts.googleapis.com/css2?family=Oswald:wght@600;700&display=swap" rel="stylesheet">
<style>
  :root {
    --cover-black: #0b0b0b;
    --cover-black-soft: #1a1a1a;
    --title-gold: #f2c12e;
    --title-amber: #e9a12a;
    --title-orange: #e5781f;
    --artist-red: #e2604b;
  }
  html, body {
    margin: 0;
    padding: 0;
    width: 1200px;
    height: 1200px;
    overflow: hidden;
    background: var(--cover-black);
  }
  .cover {
    position: relative;
    width: 1200px;
    height: 1200px;
    background: radial-gradient(circle at 50% 45%, var(--cover-black-soft) 0%, var(--cover-black) 75%);
    font-family: "Oswald", "Arial Narrow", sans-serif;
    text-align: center;
  }
  .album-title {
    position: absolute;
    top: 190px;
    left: 0;
    right: 0;
    margin: 0;
    font-weight: 700;
    text-transform: uppercase;
    line-height: 1;
  }
  .album-title__line {
    display: block;
    background: linear-gradient(135deg, var(--title-gold) 0%, var(--title-amber) 45%, var(--title-orange) 100%);
    -webkit-background-clip: text;
    background-clip: text;
    color: transparent;
  }
  .album-title__line--first {
    font-size: 250px;
    letter-spacing: 4px;
  }
  .album-title__line--second {
    font-size: 245px;
    letter-spacing: 2px;
    margin-top: -10px;
  }
  .artist-name {
    position: absolute;
    top: 820px;
    left: 0;
    right: 0;
    margin: 0;
    font-weight: 600;
    font-size: 200px;
    line-height: 1;
    color: var(--artist-red);
    text-transform: lowercase;
  }
</style>
</head>
<body>
  <main class="cover">
    <h1 class="album-title">
      <span class="album-title__line album-title__line--first">Folded</span>
      <span class="album-title__line album-title__line--second">Lanterns</span>
    </h1>
    <p class="artist-name">ned valko</p>
  </main>
</body>
</html>
```